Bref créative
Lemon Badger
Cakes and Desserts
Bright & Fun-filled
Marla Tevison
Owner
2193 Brennick Ct.
Arvada, CO 80005
marla.tevison@postvale.net
Join us on Facebook!
I also need stationery that ties in with my business card.
Logo for cake company

```html
<!DOCTYPE html>
<html lang="en">
<head>
<meta charset="utf-8">
<title>Lemon Badger – Business Cards</title>
<link href="https://fonts.googleapis.com/css2?family=Nunito:wght@400;700;800&display=swap" rel="stylesheet">
<style>
  :root {
    --bg: #efe9e2;
    --pink: #e8409e;
    --pink-dark: #c92d86;
    --brown: #8a3a10;
    --brown-text: #6b3415;
    --white: #ffffff;
    --cream: #fdf6f0;
  }
  * { box-sizing: border-box; margin: 0; padding: 0; }
  html, body {
    width: 1200px; height: 646px; overflow: hidden;
    background: var(--bg);
    font-family: "Nunito", sans-serif;
  }
  .canvas {
    position: relative; width: 1200px; height: 646px;
    display: flex; align-items: center; justify-content: center; gap: 60px;
  }
  .card {
    position: relative; width: 520px; height: 300px;
    border-radius: 6px; overflow: hidden;
    box-shadow: 0 6px 18px rgba(0,0,0,.15);
  }
  .card--front { background: var(--pink); }
  .card--back { background: var(--brown); }
  .dot-field {
    position: absolute; inset: 0;
    background: var(--pink);
  }
  .brand-panel {
    position: absolute; left: 50%; transform: translateX(-50%);
    background: var(--white); border-radius: 10px;
    display: flex; align-items: center; gap: 16px;
    padding: 18px 28px;
  }
  .card--front .brand-panel { top: 86px; }
  .card--back .brand-panel { top: 46px; }
  .brand-mark {
    width: 58px; height: 58px; border-radius: 50%;
    background: var(--pink); flex-shrink: 0;
  }
  .brand-text { display: flex; flex-direction: column; }
  .brand-name {
    font-weight: 800; font-size: 34px; line-height: 1;
    color: var(--brown-text); white-space: nowrap;
  }
  .brand-tagline {
    margin-top: 6px; font-weight: 700; font-size: 15px;
    color: var(--pink-dark); letter-spacing: .5px;
  }
  .website {
    position: absolute; left: 0; right: 0; bottom: 62px;
    text-align: center; color: var(--white);
    font-weight: 700; font-size: 13px; letter-spacing: 1px;
  }
  .contact {
    position: absolute; left: 0; right: 0; top: 176px;
    text-align: center; color: var(--white);
  }
  .contact__name { font-weight: 800; font-size: 22px; }
  .contact__line { font-size: 13px; margin-top: 6px; opacity: .92; }
  .contact__name + .contact__line { margin-top: 12px; }
</style>
</head>
<body>
  <main class="canvas">
    <section class="card card--front">
      <div class="dot-field" role="img" aria-label="Pink polka dot pattern"></div>
      <div class="brand-panel">
        <span class="brand-mark"></span>
        <div class="brand-text">
          <span class="brand-name">Lemon Badger</span>
          <span class="brand-tagline">cakes &amp; desserts</span>
        </div>
      </div>
      <p class="website">www.lemonbadgercakes.com</p>
    </section>

    <section class="card card--back">
      <div class="brand-panel">
        <span class="brand-mark"></span>
        <div class="brand-text">
          <span class="brand-name">Lemon Badger</span>
          <span class="brand-tagline">cakes &amp; desserts</span>
        </div>
      </div>
      <div class="contact">
        <p class="contact__name">Marla Tevison</p>
        <p class="contact__line">(720) 555-0142</p>
        <p class="contact__line">marla.tevison@postvale.net</p>
      </div>
    </section>
  </main>
</body>
</html>
```